Business Card needed for International Migration and Education business

we are based in Australia, the business is called 'Brightpath Migration' and its sister business for international education is called 'Brightpath Studies' - we need the design for the business 'Brightpath Migration' - Brightpath Migration is about migration to Australia (but not limited to Australia only therefore purely Australian look would not fit). We would like to see designs that use the color blue or acqua and maybe orange..all those colours don't have to be used together and not only those colours are to be used. We are looking for a modern design. The final design should communicate modern thinking, professionalism, dynamism, confidence. We would like to use the same business card design for our sister business "Brightpath Studies" - which is business about studying in different countries as we recruit students to study in Australia, USA, New Zealand, Canada, UK etc. We would like to be able the final design to be easily changed by us to fit the 'Brightpath Studies' business - we would only change the contact text (email address etc)

The information to be included in the business card: Rosalind Tepperly Managing Director Migration Agent MARN 0719264 Brightpath Migration postal address: PO Box 2274, Fernvale South VIC 3195, Australia mobile: 0417296385 office address: Level 1, 287 Corran Street, Tullagrove VIC 3211 web www.brightpathmigration.example telephone: 61 3 8574 3162 fax + 61 3 8539 7041 email: rosalind@brightpathmigration.example

Industry/Entity Type

Education

```html
<!DOCTYPE html>
<html lang="en">
<head>
<meta charset="utf-8">
<title>Brightpath Migration – Business Card</title>
<link rel="stylesheet" href="https://fonts.googleapis.com/css2?family=Open+Sans:wght@300;400;600;700&display=swap">
<style>
  :root {
    --page-bg: #e9e9e9;
    --card-bg: #ffffff;
    --brown: #6b4636;
    --orange: #f26a1f;
    --teal: #1fa5b3;
    --gold: #f7c33d;
    --crimson: #a5164b;
    --map-tint: #fdeee3;
  }
  * { margin: 0; padding: 0; box-sizing: border-box; }
  html, body {
    width: 1200px; height: 1000px; overflow: hidden;
    background: var(--page-bg);
    font-family: "Open Sans", sans-serif;
  }
  .stage {
    width: 1200px; height: 1000px;
    display: flex; align-items: center; justify-content: center;
  }
  .card {
    position: relative;
    width: 1000px; height: 572px;
    background: var(--card-bg);
    overflow: hidden;
    box-shadow: 0 10px 30px rgba(0,0,0,.15);
  }
  .map-area {
    position: absolute; right: 0; top: 0;
    width: 400px; height: 572px;
    background: radial-gradient(ellipse at 60% 55%, var(--map-tint) 0%, var(--map-tint) 55%, rgba(253,238,227,0) 75%);
  }
  .brand-band {
    position: absolute; left: 0; top: 40px;
    width: 590px; height: 88px;
    background: var(--brown);
    display: flex; align-items: center;
    padding-left: 40px;
  }
  .brand-name {
    color: var(--orange); font-weight: 700; font-size: 48px; letter-spacing: .5px;
    white-space: nowrap;
  }
  .name-tag {
    position: absolute; left: 360px; top: 110px;
    width: 440px; height: 62px;
    background: var(--teal);
    display: flex; align-items: center; padding-left: 28px;
  }
  .person-name { color: var(--gold); font-weight: 600; font-size: 36px; white-space: nowrap; }
  .credentials {
    position: absolute; left: 372px; top: 182px;
    font-weight: 600; font-size: 21px; line-height: 30px;
    white-space: nowrap;
  }
  .credentials .role { color: var(--brown); }
  .credentials .postal { color: var(--crimson); }
  .contact-list {
    position: absolute; left: 60px; top: 290px;
    list-style: none;
  }
  .contact-item {
    display: flex; align-items: center; gap: 14px;
    color: var(--crimson); font-weight: 600; font-size: 29px;
    height: 48px; white-space: nowrap;
  }
  .contact-item svg { width: 34px; height: 34px; flex: none; }
  .office { height: 60px; }
  .office-text { display: flex; flex-direction: column; line-height: 1.15; }
  .office-label { color: var(--brown); font-weight: 700; font-size: 19px; }
  .office-line { color: var(--crimson); font-weight: 400; font-size: 21px; }
</style>
</head>
<body>
<main class="stage">
  <article class="card">
    <div class="map-area" role="img" aria-label="Faint world map with an upward arrow"></div>

    <header class="brand-band">
      <span class="brand-name">Brightpath Migration</span>
    </header>

    <div class="name-tag"><span class="person-name">Rosalind Tepperly</span></div>

    <div class="credentials">
      <div class="role">Managing Director Migration Agent</div>
      <div class="role">MARN 0719264 Brightpath Migration</div>
      <div class="postal">PO Box 2274, Fernvale South VIC 3195</div>
    </div>

    <ul class="contact-list">
      <li class="contact-item office">
        <svg viewBox="0 0 36 36" aria-hidden="true"><rect x="16" y="6" width="4" height="26" fill="var(--orange)"/><path d="M4 8h24l5 5-5 5H4z" fill="var(--orange)"/><rect x="10" y="31" width="16" height="4" rx="2" fill="var(--orange)"/></svg>
        <span class="office-text">
          <span class="office-label">Office address</span>
          <span class="office-line">Level 1, 287 Corran Street, Tullagrove VIC 3211</span>
        </span>
      </li>
      <li class="contact-item">
        <svg viewBox="0 0 36 36" aria-hidden="true"><rect x="11" y="3" width="14" height="30" rx="3" fill="var(--orange)"/><rect x="14" y="7" width="8" height="18" fill="#fff"/></svg>
        <span>0417296385 &nbsp;/ +613 8574 3162</span>
      </li>
      <li class="contact-item">
        <svg viewBox="0 0 36 36" aria-hidden="true"><rect x="4" y="14" width="28" height="18" rx="3" fill="var(--orange)"/><rect x="10" y="4" width="16" height="12" fill="var(--orange)"/><rect x="12" y="6" width="12" height="8" fill="#fff"/><rect x="9" y="20" width="18" height="3" fill="#fff"/></svg>
        <span>+613 8539 7041</span>
      </li>
      <li class="contact-item">
        <svg viewBox="0 0 36 36" aria-hidden="true"><circle cx="18" cy="18" r="14" fill="none" stroke="var(--orange)" stroke-width="3"/><ellipse cx="18" cy="18" rx="6" ry="14" fill="none" stroke="var(--orange)" stroke-width="2.5"/><line x1="4" y1="18" x2="32" y2="18" stroke="var(--orange)" stroke-width="2.5"/></svg>
        <span>www.brightpathmigration.example</span>
      </li>
      <li class="contact-item">
        <svg viewBox="0 0 36 36" aria-hidden="true"><rect x="3" y="8" width="30" height="20" fill="none" stroke="var(--orange)" stroke-width="3"/><path d="M3 8l15 12 15-12" fill="none" stroke="var(--orange)" stroke-width="3"/></svg>
        <span>rosalind@brightpathmigration.example</span>
      </li>
    </ul>
  </article>
</main>
</body>
</html>
```